Social Media Graphics - Copperfield Loop

Create 6-7 individual social media graphics (square size) to encourage folks to join our online course, using either of the text below (only one set of text per graphic:

The Lantern Ridge Method
How to Create a 7-Figure Business From Scratch
Sign Up Today!

Or

The Lantern Ridge Method
Fast-track Your Way to a Multi-Million Business!
Sign Up Today!

For the color scheme of the graphics, use 1 or 2 colors in the color palette attached; or use any colors that look nice with their outfits; AVOID using red, white and blue altogether because it will look like an Independence Day (4th of July) graphic and we don’t want that; make sure the graphics appeal to both men and women

Make sure each graphic contains 1 of the 2 pics attached; and make sure one of the graphics is all TEXT only.

Target Market(s)

men and women looking to make more money

Industry/Entity Type

entrepreneurship

Requirements
Must have
• see the text document attached
Nice to have
• We are open to a nice color design; the color palette colors are not required, especially we don't want red, white and blue used together
Should not have
• AVOID using red, white and blue altogether because it will look like an Independence Day (4th of July) graphic and we dont want that

```html
<!DOCTYPE html>
<html lang="en">
<head>
<meta charset="utf-8">
<title>Copperfield Loop – Social Graphics</title>
<link rel="stylesheet" href="https://fonts.googleapis.com/css2?family=Oswald:wght@500;700&display=swap">
<style>
  :root {
    --canvas: #2b0710;
    --red: #d7192b;
    --red-deep: #9e0f1d;
    --pink: #f7c9d4;
    --pink-soft: #fde6ec;
    --plum: #4a1457;
    --plum-deep: #26082f;
    --gold: #f3c04a;
    --white: #ffffff;
    --ink: #1c1c2a;
    --photo-a: #5a3a30;
    --photo-b: #c98a78;
  }
  * { box-sizing: border-box; margin: 0; padding: 0; }
  html, body { width: 893px; height: 1200px; overflow: hidden; }
  body { background: var(--canvas); font-family: "Oswald", "Arial Narrow", sans-serif; text-transform: uppercase; }
  .board { position: relative; width: 893px; height: 1200px; }
  .tile { position: absolute; width: 277px; height: 270px; overflow: hidden; }
  .col-a { left: 155px; } .col-b { left: 461px; }
  .row-1 { top: 140px; } .row-2 { top: 447px; } .row-3 { top: 750px; }
  .abs { position: absolute; }
  .title { font-weight: 700; font-size: 17px; line-height: 1; letter-spacing: .2px; }
  .pitch { font-weight: 700; line-height: 1.02; }
  .cta { font-weight: 700; font-size: 15px; line-height: 1.2; }
  .photo { background: radial-gradient(circle at 45% 35%, var(--photo-b), var(--photo-a) 75%); }

  /* tile 1 */
  .t1 { background: linear-gradient(135deg, var(--red) 0%, var(--red-deep) 100%); }
  .t1 .title { left: 16px; top: 16px; color: var(--white); }
  .t1 .pitch { left: 16px; top: 60px; width: 120px; font-size: 20px; color: var(--white); }
  .t1 .photo { right: 10px; top: 50px; width: 124px; height: 124px; border-radius: 50%; border: 5px solid var(--white); }
  .t1 .cta { left: 0; right: 0; bottom: 20px; text-align: right; padding-right: 16px; color: var(--white); font-size: 18px; }

  /* tile 2 */
  .t2 { background: linear-gradient(160deg, var(--pink-soft), var(--pink)); }
  .t2 .title { left: 0; right: 0; top: 28px; text-align: center; color: var(--ink); }
  .t2 .pitch { left: 16px; right: 16px; top: 62px; text-align: center; font-size: 30px; color: var(--red-deep); }
  .t2 .cta { left: 50%; transform: translateX(-50%); bottom: 34px; background: var(--red); color: var(--white); padding: 5px 20px; font-size: 17px; white-space: nowrap; }

  /* tile 3 */
  .t3 { background: linear-gradient(135deg, var(--plum), var(--plum-deep)); }
  .t3 .title { left: 16px; top: 20px; color: var(--white); font-size: 19px; width: 150px; }
  .t3 .pitch { left: 16px; top: 76px; width: 126px; font-size: 22px; color: var(--gold); }
  .t3 .photo { right: 0; bottom: 0; width: 122px; height: 196px; }
  .t3 .cta { left: 16px; bottom: 14px; background: var(--white); color: var(--plum); padding: 3px 10px; }

  /* tile 4: text only */
  .t4 { background: linear-gradient(135deg, var(--plum), var(--plum-deep)); border: 4px solid var(--gold); }
  .t4 .title { left: 10px; right: 10px; top: 36px; text-align: center; color: var(--white); font-size: 30px; line-height: 1.08; }
  .t4 .band { left: 20px; right: 20px; top: 128px; background: var(--gold); color: var(--plum-deep); text-align: center; padding: 9px 8px; font-size: 16px; }
  .t4 .cta { left: 0; right: 0; bottom: 36px; text-align: center; color: var(--white); font-size: 17px; }

  /* tile 5 */
  .t5 { background: linear-gradient(160deg, var(--red), var(--red-deep)); }
  .t5 .title { left: 0; right: 0; top: 14px; text-align: center; color: var(--white); }
  .t5 .photo { left: 40px; right: 40px; top: 38px; height: 104px; }
  .t5 .band { left: 22px; right: 22px; top: 134px; background: var(--ink); color: var(--white); text-align: center; padding: 8px 6px; font-size: 17px; }
  .t5 .cta { left: 50%; transform: translateX(-50%); bottom: 14px; background: var(--red); border: 2px solid var(--white); color: var(--white); padding: 2px 18px; border-radius: 14px; font-size: 14px; white-space: nowrap; }

  /* tile 6 */
  .t6 { background: linear-gradient(135deg, var(--pink-soft), var(--pink)); }
  .t6 .title { left: 0; right: 0; top: 18px; text-align: center; color: var(--red-deep); }
  .t6 .pitch { left: 16px; top: 64px; width: 110px; font-size: 17px; color: var(--red-deep); font-weight: 500; }
  .t6 .photo { right: 0; bottom: 0; width: 145px; height: 210px; }
  .t6 .cta { left: 16px; top: 176px; width: 100px; color: var(--red); font-size: 21px; line-height: 1.02; }
</style>
</head>
<body>
<main class="board">
  <section class="tile t1 col-a row-1">
    <p class="abs title">The Lantern Ridge Method</p>
    <p class="abs pitch">Fast-Track your way to a Multi-Million Business!</p>
    <div class="abs photo" role="img" aria-label="Circular portrait of the two course hosts"></div>
    <p class="abs cta">Sign Up Today!</p>
  </section>

  <section class="tile t2 col-b row-1">
    <p class="abs title">The Lantern Ridge Method</p>
    <p class="abs pitch">How to Create a 7-Figure Business from Scratch</p>
    <p class="abs cta">Sign Up Today!</p>
  </section>

  <section class="tile t3 col-a row-2">
    <p class="abs title">The Lantern Ridge Method</p>
    <p class="abs pitch">Fast-Track your way to a Multi-Million Business!</p>
    <div class="abs photo" role="img" aria-label="Photo of the two course hosts standing together"></div>
    <p class="abs cta">Sign Up Today!</p>
  </section>

  <section class="tile t4 col-b row-2">
    <p class="abs title">The Lantern Ridge<br>Method</p>
    <p class="abs band pitch">Fast-Track your way to a Multi-Million Business!</p>
    <p class="abs cta">Sign Up Today!</p>
  </section>

  <section class="tile t5 col-a row-3">
    <p class="abs title">The Lantern Ridge Method</p>
    <div class="abs photo" role="img" aria-label="Photo of the two course hosts side by side"></div>
    <p class="abs band pitch">How to Create a 7-Figure Business from Scratch</p>
    <p class="abs cta">Sign Up Today!</p>
  </section>

  <section class="tile t6 col-b row-3">
    <p class="abs title">The Lantern Ridge Method</p>
    <p class="abs pitch">Fast-Track your way to a Multi-Million Business!</p>
    <div class="abs photo" role="img" aria-label="Photo of the two course hosts, woman in front"></div>
    <p class="abs cta">Sign Up Today!</p>
  </section>
</main>
</body>
</html>
```